Penny auctions banner design to get people to sign up

Show the 3 steps needed to get started bidding with penny auctions on my website ZelNork.com. The core colors should be black, grey, and yellow.

It needs to show the following steps: 1) Register an account. 2) Purchase the starter package. 3) Start bidding and save up to 98% off!

Some creativity would be good so if you have some better ideas then please let them flow and show me your best banner design :) Thank you! Comment with any questions you have. Attached is my logo.

```html
<!DOCTYPE html>
<html lang="en">
<head>
<meta charset="utf-8">
<title>ZelNork.com – Penny Auction Banner</title>
<link rel="stylesheet" href="https://fonts.googleapis.com/css2?family=PT+Sans:wght@700&display=swap">
<style>
  :root {
    --page-bg: #ffffff;
    --page-edge: #ececec;
    --panel-black: #1c1c1c;
    --panel-black-deep: #0f0f0f;
    --accent-yellow: #f5c400;
    --accent-yellow-light: #ffe14a;
    --side-grey: #eeeeee;
    --side-grey-dark: #d9d9d9;
    --frame-grey: #cfcfcf;
    --text-white: #ffffff;
    --text-dark: #1a1a1a;
  }
  * { box-sizing: border-box; margin: 0; padding: 0; }
  html, body { width: 1200px; height: 574px; overflow: hidden; }
  body {
    background: radial-gradient(ellipse at center, var(--page-bg) 45%, var(--page-edge) 100%);
    font-family: "PT Sans", "Arial Narrow", sans-serif;
    position: relative;
  }
  .banner {
    position: absolute;
    left: 216px; top: 193px;
    width: 768px; height: 188px;
    border: 1px solid var(--frame-grey);
    background: linear-gradient(180deg, var(--side-grey), var(--side-grey-dark));
    overflow: hidden;
  }
  .banner-shape { position: absolute; inset: 0; }
  .steps {
    position: absolute;
    left: 40px; width: 560px; top: 0;
    list-style: none;
    color: var(--text-white);
    text-align: center;
    font-size: 25px;
    line-height: 1;
    text-transform: uppercase;
    letter-spacing: 0.2px;
  }
  .step { position: absolute; left: 0; right: 0; }
  .step-1 { top: 8px; }
  .step-2 { top: 60px; }
  .step-3 { top: 103px; line-height: 36px; }
  .highlight { color: var(--accent-yellow); }
  .brand {
    position: absolute;
    left: 622px; width: 146px; top: 12px;
    display: flex; flex-direction: column; align-items: center;
  }
  .brand-dot {
    width: 40px; height: 40px; border-radius: 50%;
    background: var(--text-dark);
  }
  .brand-name {
    margin-top: 6px;
    font-size: 30px; line-height: 1;
    color: var(--text-dark);
  }
  .go-button {
    position: absolute;
    left: 628px; top: 123px;
    width: 121px; height: 49px;
    border-radius: 25px;
    background: linear-gradient(180deg, var(--accent-yellow-light), var(--accent-yellow));
    box-shadow: 0 2px 3px rgba(0,0,0,0.25);
    display: flex; align-items: center; justify-content: center; gap: 8px;
    color: var(--text-dark);
    font-size: 32px; text-decoration: none;
  }
  .go-arrow { width: 18px; height: 22px; }
</style>
</head>
<body>
  <div class="banner">
    <svg class="banner-shape" viewBox="0 0 768 188" width="768" height="188" aria-hidden="true">
      <defs>
        <radialGradient id="panelGlow" cx="50%" cy="35%" r="70%">
          <stop offset="0" stop-color="var(--panel-black)"/>
          <stop offset="1" stop-color="var(--panel-black-deep)"/>
        </radialGradient>
      </defs>
      <path d="M0 0 H612 Q568 94 612 188 H0 Z" fill="var(--accent-yellow)"/>
      <path d="M40 0 H604 Q560 94 604 188 H40 Q4 94 40 0 Z" fill="url(#panelGlow)"/>
      <path d="M0 0 H40 Q4 94 40 188 H0 Z" fill="var(--accent-yellow)"/>
      <path d="M0 0 H22 Q-8 94 22 188 H0 Z" fill="var(--side-grey)"/>
    </svg>
    <ol class="steps">
      <li class="step step-1">1. Register an account.</li>
      <li class="step step-2">2. Purchase the starter package.</li>
      <li class="step step-3">3 Start bidding and save<br>up to <span class="highlight">98%</span> off!</li>
    </ol>
    <div class="brand">
      <span class="brand-dot"></span>
      <span class="brand-name">ZelNork</span>
    </div>
    <a class="go-button" href="#">GO
      <svg class="go-arrow" viewBox="0 0 18 22" aria-hidden="true"><path d="M2 1 L17 11 L2 21 Z" fill="var(--text-dark)"/></svg>
    </a>
  </div>
</body>
</html>
```